Top International Talent Management Needs creative business card design

We manage actors careers and book them liaising and promoting their profiles internationally through Casting Directors, Producers, Directors, Publicists etc. We need clearly visable contact details but with a design that reflects our status and creativity of TV, Feature Film industry. Our logo is attached and needs to relate and our website is www.quillbrookstagefolk.com
No flame designs please but please incorporate logo colours.

Target Market(s)

Clients

Industry/Entity Type

Film Production

Contact Information for Business Card

Director Rosalind Pettigrew
Suite D, Building 7, Harbourlight Lots Australia, Wren Flats, Sydney, NSW 2048

Font styles to use
Sans Serif

Colors
ec1f27

Requirements
Nice to have
• Colours should relate to logo attached and type can relate again to type in the logo design.
Should not have
• No Flames designs and best to be not too obvious with the film designs eiither. Needs to be more creative and modern

```html
<!DOCTYPE html>
<html lang="en">
<head>
<meta charset="utf-8">
<title>Quillbrook Stagefolk — Business Card</title>
<link rel="stylesheet" href="https://fonts.googleapis.com/css2?family=Open+Sans:wght@400;600;700&display=swap">
<style>
  :root {
    --brand-red: #ec1f27;
    --deep-red: #b5121a;
    --ink: #1a1a1a;
    --card-black: #141414;
    --card-black-soft: #262626;
    --paper: #ffffff;
    --stage-grey: #8a8a8a;
    --text-light: #f2f2f2;
    --backdrop-top: #c9c9c9;
    --backdrop-bottom: #7d7d7d;
  }
  * { box-sizing: border-box; margin: 0; padding: 0; }
  html, body { width: 1200px; height: 900px; overflow: hidden; }
  body {
    font-family: "Open Sans", sans-serif;
    background: linear-gradient(180deg, var(--backdrop-top) 0%, var(--backdrop-bottom) 100%);
    position: relative;
  }
  .card {
    position: absolute;
    top: 300px;
    width: 525px;
    height: 300px;
    border-radius: 22px;
    overflow: hidden;
    box-shadow: 0 18px 40px rgba(0,0,0,0.35);
  }
  .card--front { left: 50px; background: var(--card-black); }
  .card--back {
    left: 625px;
    background: radial-gradient(ellipse at 50% 45%, var(--card-black-soft) 0%, var(--card-black) 70%);
    display: flex; align-items: center; justify-content: center;
  }
  .front-header {
    position: absolute; left: 0; top: 0; width: 100%; height: 150px;
    background: var(--paper);
  }
  .production-artwork {
    position: absolute; right: 0; top: 0; width: 210px; height: 150px;
    background: linear-gradient(135deg, rgba(255,255,255,0) 0%, #d6d6d6 45%, var(--stage-grey) 100%);
  }
  .person-name {
    position: absolute; right: 30px; top: 18px;
    color: var(--brand-red); font-weight: 600; font-size: 19px; text-align: right;
  }
  .person-role {
    position: absolute; right: 30px; top: 44px;
    color: var(--ink); font-size: 13px;
  }
  .wordmark {
    font-weight: 700; color: var(--brand-red); letter-spacing: 0.5px;
  }
  .front-header .wordmark {
    position: absolute; left: 22px; top: 72px; font-size: 30px;
  }
  .divider-band {
    position: absolute; left: 0; top: 150px; width: 100%; height: 14px;
    background: linear-gradient(180deg, var(--brand-red) 0%, var(--deep-red) 70%, #c0c0c0 70%, #9a9a9a 100%);
  }
  .contact-list {
    position: absolute; left: 22px; top: 184px; list-style: none;
    color: var(--text-light); font-size: 12.5px; line-height: 17px;
  }
  .contact-list li { display: flex; align-items: flex-start; gap: 6px; }
  .contact-list svg { flex: none; margin-top: 3px; }
  .social-slots {
    position: absolute; right: 38px; bottom: 36px; display: flex; gap: 6px;
  }
  .social-slot {
    width: 26px; height: 26px; border-radius: 4px; background: var(--brand-red);
  }
  .card--back .wordmark { font-size: 40px; }
</style>
</head>
<body>
  <section class="card card--front" aria-label="Card front">
    <div class="front-header">
      <div class="production-artwork" role="img" aria-label="Faded film production equipment artwork"></div>
      <p class="person-name">Rosalind Pettigrew</p>
      <p class="person-role">Director</p>
      <p class="wordmark">Quillbrook Stagefolk</p>
    </div>
    <div class="divider-band"></div>
    <ul class="contact-list">
      <li>
        <svg width="10" height="10" viewBox="0 0 10 10"><path d="M2 0.5 L3.6 2.8 L2.6 3.9 Q3.8 6.2 6.1 7.4 L7.2 6.4 L9.5 8 L8.3 9.5 Q2.5 9 0.5 1.7 Z" fill="var(--brand-red)"/></svg>
        <span>+61(0)400316274</span>
      </li>
      <li>
        <svg width="10" height="10" viewBox="0 0 10 10"><rect x="0.5" y="2" width="9" height="6.5" fill="var(--brand-red)"/><path d="M0.5 2 L5 5.6 L9.5 2" stroke="var(--card-black)" fill="none"/></svg>
        <span>talent@quillbrookstagefolk.com</span>
      </li>
      <li>
        <svg width="10" height="10" viewBox="0 0 10 10"><circle cx="5" cy="5" r="4.3" fill="none" stroke="var(--brand-red)" stroke-width="1.2"/><path d="M0.7 5 H9.3 M5 0.7 Q2.5 5 5 9.3 M5 0.7 Q7.5 5 5 9.3" stroke="var(--brand-red)" fill="none"/></svg>
        <span>www.quillbrookstagefolk.com</span>
      </li>
      <li>
        <svg width="10" height="10" viewBox="0 0 10 10"><path d="M5 0.5 L9.5 4.6 H8.2 V9.5 H1.8 V4.6 H0.5 Z" fill="var(--brand-red)"/></svg>
        <span>Suite D, Building 7, Harbourlight Lots Australia,<br>Wren Flats, Sydney, NSW 2048</span>
      </li>
    </ul>
    <div class="social-slots">
      <span class="social-slot"></span>
      <span class="social-slot"></span>
    </div>
  </section>

  <section class="card card--back" aria-label="Card back">
    <p class="wordmark">Quillbrook Stagefolk</p>
  </section>
</body>
</html>
```